Backup Software Tri-fold Brochure Project

We need a great looking and informative brochure to describe our new Backup Software offering. The brochures are to be used in retail and small business environments given to clients interested in protecting their computer from data loss.
The brochure should include attractive imagery that conveys a sense of Trust and Security to the prospective client.
The copy is provided as an attachment to this project. We'd like our Bright Deskpoint product logo to be printed on the back cover. The logo is attached to this project.
The finished tri-fold brochure will be submitted to Plumcopy for printing as an 8.5" x 11" tri-fold brochure. Their design instructions are online http://plumcopy-example.com/custom-brochures.aspx.
The finished product should be Adobe Illustrator CS3 (*.ai) with a PDF Proof.
Target Market(s)
Retail and Small Business customers
Industry/Entity Type
Software
Designer to choose colors to be used in the design.

```html
<!DOCTYPE html>
<html lang="en">
<head>
<meta charset="utf-8">
<title>Bright Deskpoint Offsite Backup – Tri-fold Brochure</title>
<link rel="stylesheet" href="https://fonts.googleapis.com/css2?family=Roboto+Condensed:ital,wght@0,300;0,400;0,700;1,400;1,700&family=Roboto:wght@300;400&display=swap">
<style>
  :root{
    --stage:#0d4f7a;
    --paper:#ffffff;
    --ink:#1d1d1d;
    --brand-blue:#1a5ea8;
    --brand-navy:#123a64;
    --brand-green:#6bb52f;
    --panel-blue:#1466ab;
    --panel-dark:#111622;
    --heading-green:#74b43a;
    --backup-navy:#12233f;
  }
  *{box-sizing:border-box;margin:0;padding:0}
  html,body{width:1200px;height:1200px;overflow:hidden}
  body{background:var(--stage);font-family:"Roboto Condensed",Arial,sans-serif;color:var(--ink);position:relative}
  .sheet{position:absolute;width:690px;height:535px;display:flex;background:var(--paper);box-shadow:0 10px 20px rgba(0,0,0,.35)}
  .sheet--inside{left:45px;top:48px}
  .sheet--outside{left:418px;top:614px}
  .panel{position:relative;width:230px;height:100%;overflow:hidden}
  .brand-name{font-family:"Roboto Condensed",Arial,sans-serif;font-weight:700;color:var(--brand-blue);font-size:23px;line-height:1;display:flex;align-items:center;gap:7px}
  .brand-name::before{content:"";width:14px;height:14px;background:var(--brand-green);flex:none}
  .body-copy{font-size:8.5px;line-height:1.36;text-align:justify;color:var(--ink)}
  .body-copy p+p{margin-top:10px}
  /* inside sheet */
  .intro{padding:40px 16px 0 22px}
  .intro .lead{font-size:9.8px;line-height:1.38;margin-top:38px;margin-bottom:12px}
  .tagline{position:absolute;left:22px;top:426px;font-size:18px;font-weight:300;line-height:1.55}
  .tagline strong{font-weight:700;font-style:italic;font-size:23px}
  .offer{padding:26px 16px 0 18px}
  .offer h2{font-family:Roboto,Arial,sans-serif;font-weight:400;font-size:25px;line-height:1.25;color:var(--heading-green);margin-bottom:14px}
  .offer h2 span{color:var(--brand-blue)}
  .offer h3{font-size:15px;line-height:1.35;color:var(--brand-navy);font-weight:700;margin-top:22px;margin-bottom:12px}
  .feature-list{list-style:none;font-size:8.8px;line-height:1.45;color:var(--brand-blue)}
  .feature-list li{padding-left:7px;text-indent:-6px;margin-bottom:12px}
  .photo{position:absolute}
  .photo--office{inset:0;background:linear-gradient(160deg,#eef1f6 0%,#f3e2d3 30%,#f5d9d8 55%,#ececf0 100%)}
  /* outside sheet */
  .how{background:linear-gradient(#111622 0,#1a1420 60%,#fff 60%)}
  .how__head{padding:22px 14px 0 18px;color:#fff}
  .how__head h2{font-family:Roboto,Arial,sans-serif;font-weight:300;font-size:24px;margin-bottom:6px}
  .how__head p{font-size:11px;line-height:1.3}
  .photo--tech{left:0;top:108px;width:230px;height:250px;background:radial-gradient(circle at 50% 40%,#e8a7bf 0%,#b2395f 30%,#4a1a33 60%,#f4eef2 100%)}
  .how__body{position:absolute;left:20px;right:12px;top:365px;font-size:8.2px;line-height:1.4;text-align:left}
  .how__body p+p{margin-top:10px}
  .format{background:var(--panel-blue);color:#fff}
  .format__banner{position:absolute;left:0;right:0;top:44px;height:44px;background:var(--brand-green);font-style:italic;font-weight:700;font-size:11px;line-height:1.4;text-align:center;padding-top:6px}
  .format__lead{position:absolute;left:8px;right:8px;top:96px;text-align:center;font-size:13px;line-height:1.3}
  .format__curve{position:absolute;left:0;top:0}
  .photo--drive{left:92px;top:230px;width:115px;height:110px;border-radius:8px;background:linear-gradient(#e7e9ec,#9ea3a9)}
  .format__cta{position:absolute;left:18px;right:10px;top:404px;font-size:12px;line-height:1.35}
  .format__cta small{display:block;font-size:8.2px;line-height:1.4;margin-top:3px}
  .format__cta small b{color:var(--brand-green);font-weight:400;font-size:10px}
  .format__phone{position:absolute;left:0;right:0;top:474px;text-align:center;font-size:30px;font-weight:700;letter-spacing:.5px}
  .format__legal{position:absolute;left:0;right:0;top:513px;text-align:center;font-size:6.6px}
  .cover{background:linear-gradient(180deg,#fff 0%,#eef6e3 25%,#d9ecc0 45%,#d5e7f3 70%,#c2dcef 100%)}
  .cover .brand-name{position:absolute;left:26px;top:44px;font-size:21px}
  .cover h2{position:absolute;left:28px;top:118px;font-family:Roboto,Arial,sans-serif;font-weight:400;font-size:19px;line-height:1.2;color:var(--ink)}
  .stats{position:absolute;left:32px;top:177px;font-size:9.4px;line-height:1.5}
  .stats b{font-weight:700;font-size:9.6px}
  .stats ul{list-style:none;padding-left:8px;font-size:8.3px;line-height:1.7}
  .photo--worried{left:16px;top:256px;width:214px;height:160px;background:linear-gradient(135deg,#dfe8ee 0%,#c5d3dc 45%,#2b2f36 75%,#1c1f25 100%)}
  .cover__tag{position:absolute;left:30px;top:455px;color:var(--backup-navy)}
  .cover__tag span{display:block;font-style:italic;font-weight:700;font-size:14px}
  .cover__tag strong{display:block;font-size:47px;font-weight:700;line-height:1;letter-spacing:.5px}
</style>
</head>
<body>

<section class="sheet sheet--inside">
  <div class="panel intro">
    <div class="brand-name">Bright Deskpoint</div>
    <p class="body-copy lead">Your computer stores everything you've ever created. Everything you've written, every email you've sent, every list you've made, every picture you've taken or movie you've made, all music you've created, your proposals, your spreadsheets, your presentations, your word files, your artwork, programs you've written, anything you've dictated, and much more...</p>
    <div class="body-copy">
      <p>All your digital life is stored on your computer and is at risk of loss without backup.</p>
      <p>And your computer stores a copy of all your personal information. Your passwords, your online banking, your PINs, your credit cards and all your health and shopping records. This makes it a juicy target for hackers. Every day your digital life is exposed to computer Viruses, Malware and spammers all trying to break in. If they succeed the damage could be incalculable.<br>If hackers destroy your information or a simple hard drive failure happens, restoring your programs will cost you days of effort and potentially hundreds of dollars. But your files could be unrecoverable. This means the loss of everything you've ever created.</p>
    </div>
    <p class="tagline">The only protection is<br>a great <strong>BACKUP.</strong></p>
  </div>

  <div class="panel offer">
    <h2>We Have<br><span>What You Need</span></h2>
    <div class="body-copy">
      <p>We can create a snapshot of all the programs and files on your computer using our Image Backup technology. We'll give you your backup on an external hard drive which you can store someplace safe. If anything happens, just bring in your computer and your Image Backup and we'll restore your computer back to the point when the snapshot was taken.</p>
      <p>Restoring from an Image Backup is like setting your computer back in time. To make sure all your new files are protected, we'll also install Harbrook-Net's Bright Deskpoint software to backup your files every night. These backups are stored in Harbrook-Net's secure datacenter to protect you from even the most severe data loss scenarios.</p>
    </div>
    <h3>OUR IMAGE BACKUP<br>TECHNOLOGY CAN PROTECT</h3>
    <ul class="feature-list">
      <li>* Casement PC's and Laptops running Casement 7 and above (Casement 8, 10+)</li>
      <li>* Casement Servers running Casement 2008 and above (Casement 2012, 2016+)</li>
    </ul>
  </div>

  <div class="panel">
    <div class="photo photo--office" role="img" aria-label="Photo of a smiling woman in a light pink blouse working on a laptop at a bright office desk"></div>
  </div>
</section>

<section class="sheet sheet--outside">
  <div class="panel how">
    <div class="how__head">
      <h2>How It Works</h2>
      <p>Our technology is designed to take advantage of the powerful imaging technology embedded in <b><i>Corvane Casement.</i></b></p>
    </div>
    <div class="photo photo--tech" role="img" aria-label="Illustration of a hand touching a glowing circuit-board hard drive icon"></div>
    <div class="how__body">
      <p>Deep within the core of the OS is an imaging engine that can create a point-in-time backup of the Casement Operating System, device drivers, programs and system state. The backup can be used later to recover the system back to this point-in-time.</p>
      <p>Backups created by our Imaging technology can even be used to restore Casement to dissimilar hardware.</p>
      <p>This is a quick way to migrate to a new computer without having to reinstall everything from scratch.</p>
    </div>
  </div>

  <div class="panel format">
    <svg class="format__curve" width="230" height="535" viewBox="0 0 230 535" aria-hidden="true">
      <path d="M0 188 C20 300 110 395 230 408 L230 430 C100 420 10 340 0 260 Z" fill="var(--panel-blue)"/>
      <path d="M0 196 C25 300 110 385 230 398 L230 210 C150 215 60 230 0 196 Z" fill="var(--brand-green)"/>
      <path d="M0 188 C20 300 110 395 230 408" fill="none" stroke="#fff" stroke-width="4"/>
    </svg>
    <div class="format__banner">Our technology stores backups as<br>Corvane "Virtual Disk Image" (VDI).</div>
    <p class="format__lead">These VDI files can be directly mounted from the Casement Disk Manager.<br>This is a great way to browse the contents of your Image Backup and restore individual files and folders.</p>
    <div class="photo photo--drive" role="img" aria-label="Illustration of a silver hard drive labelled with the disk image format"></div>
    <div class="format__cta">Call us to schedule<br>a day to bring in your computer.
      <small><b>OR</b> Once a month we do "Image Backup Saturday". Drop off your computer in the morning and pick it up a few hours later. Call for a copy of our schedule.</small>
    </div>
    <div class="format__phone">800 555 0199</div>
    <div class="format__legal">Copyright(c) 2017, Harbrook-Net, Inc. All Rights Reserved</div>
  </div>

  <div class="panel cover">
    <div class="brand-name">Bright Deskpoint</div>
    <h2>Your entire digital<br>Life is at Risk</h2>
    <div class="stats">
      <b>Every week (in the US)</b>
      <ul>
        <li>* 140,000 drives crash</li>
        <li>* 12,000 laptops are lost or stolen</li>
        <li>* 37,000 Internet Crimes are committed</li>
        <li>* Internet criminals steal $25 Million</li>
      </ul>
    </div>
    <div class="photo photo--worried" role="img" aria-label="Photo of a stressed businessman holding his head in front of a laptop"></div>
    <div class="cover__tag"><span>The only protection is a great</span><strong>BACKUP</strong></div>
  </div>
</section>

</body>
</html>
```